Develop a Corporate Identity for Hardolen.to

[login to view URL] is a new website currently under development.

This contest is to find a designer, or a team of designers, for ongoing design work on this enterprise.
We are looking for designer(s) who has good ideas and communicates well with us.

The winner will be contacted for further work :
We will provide a complete website description, and complete page-by-page design specifications will be required, for our programmers to implement.

Please submit your design/ideas that includes the following items :
1. Logo design
2. Icons design (for links, like those used in [login to view URL]) as well as for [login to view URL]
3. Website design mockup (just front page)
4. Blog design mockup
5. Coming Soon page mockup

Concepts to keep in mind :
1. This will be a website to give money to other people/entities (members of the website).
2. Members will be everyone from bloggers, YouTube personalities, charity/social/environmental/religious organizations, artists, open source developers, and ordinary people.
3. Anyone, including non-members, can give money to members. Therefore, it's convenient for them to advertise on their website (for example : "Donate to us at [login to view URL])
4. Reasons for giving money could be for supporting a good cause, or transactional (paying for something). Our focus is on supporting people/causes you like.

Optional considerations :
5. The front page should probably be informative without being confusing. Showing the trending causes/members, showing a banner for noteworthy members, showing a few success stories, etc.
6. Possibly use an indigo color

Feel free to ask any questions if you want to refine your submissions.

```html
<!DOCTYPE html>
<html lang="en">
<head>
<meta charset="utf-8">
<title>Hardolen.to</title>
<link href="https://fonts.googleapis.com/css2?family=Open+Sans:wght@400;600;700&family=Arimo:wght@400&display=swap" rel="stylesheet">
<style>
:root{
  --orange:#f7931e;
  --ink:#333;
  --grey-dark:#333;
  --grey-mid:#555;
  --grey-panel:#474747;
  --grey-circle:#8a8a8a;
  --text-grey:#666;
  --white:#fff;
}
*{margin:0;padding:0;box-sizing:border-box}
html,body{width:1200px;height:899px;overflow:hidden;background:var(--white)}
body{position:relative;font-family:"Open Sans",sans-serif;color:var(--ink)}
.page{position:absolute;left:221px;top:11px;width:803px;height:883px;background:linear-gradient(90deg,#cfcfcf,#e9e9e9 12%,#e9e9e9 88%,#cfcfcf)}
.header{position:absolute;left:221px;top:11px;width:803px;height:116px;background:linear-gradient(180deg,#fafafa,#dedede)}
.brand{position:absolute;left:264px;top:38px;display:flex;align-items:center;gap:14px}
.brand-mark{width:22px;height:22px;border-radius:50%;background:var(--text-grey)}
.brand-name{font-weight:400;font-size:40px;color:var(--text-grey);letter-spacing:.2px}
.top-links a{position:absolute;top:4px;font-size:11px;color:var(--ink);text-decoration:none}
.search{position:absolute;left:811px;top:81px;width:203px;height:36px;background:#555;padding:7px 9px 5px 6px}
.search-field{width:100%;height:100%;background:var(--white);display:flex;align-items:center;justify-content:space-between;padding:0 4px;font-size:12px;color:#999;font-family:"Arimo",sans-serif}
.banner{position:absolute;left:221px;top:127px;width:803px;height:266px;background:var(--grey-mid)}
.banner-stage{position:absolute;left:99px;top:8px;width:620px;height:235px;background:var(--grey-dark)}
.banner-strip{position:absolute;left:99px;top:243px;width:620px;height:23px;background:var(--grey-panel)}
.mascot{position:absolute;left:33px;top:6px;width:340px;height:170px;background:radial-gradient(ellipse at center,#5a5a5a,#3a3a3a 70%)}
.circle{position:absolute;border-radius:50%;background:var(--grey-circle)}
.learn-more{position:absolute;left:203px;top:185px;width:175px;height:41px;border-radius:8px;background:linear-gradient(180deg,#9a9a9a,#6c6c6c);color:var(--white);font-size:22px;display:flex;align-items:center;padding-left:11px;gap:14px}
.dots{position:absolute;left:16px;top:249px;display:flex;gap:2px}
.dots span{width:9px;height:9px;border-radius:50%;background:#aaa}
.dots .active{background:var(--white);outline:1.5px solid #222}
.next{position:absolute;left:757px;top:238px}
.social{position:absolute;left:0;top:68px;width:36px;height:96px;background:#eee;padding:5px 4px;display:flex;flex-direction:column;gap:6px}
.social span{width:26px;height:24px;background:#3b5998;border-radius:3px}
.social span:nth-child(2){background:#33a4e0}
.social span:nth-child(3){background:#2f6ea8}
.content{position:absolute;left:331px;top:395px;width:620px;height:298px;background:var(--white)}
.content h1{position:absolute;left:0;top:14px;font-family:"Arimo",sans-serif;font-weight:400;font-size:24px;color:var(--text-grey);letter-spacing:.3px}
.intro{position:absolute;left:4px;top:39px;width:580px;font-family:"Arimo",sans-serif;font-size:12.4px;line-height:15.3px;text-align:justify;color:#444}
.news{position:absolute;top:120px;width:225px;height:139px;color:var(--white)}
.news-orange{left:37px;background:var(--orange)}
.news-dark{left:320px;background:#4a4a4a;height:140px}
.news h2{position:absolute;left:10px;top:6px;font-family:"Arimo",sans-serif;font-weight:400;font-size:18px}
.news hr{position:absolute;left:50px;right:0;top:32px;border:0;border-top:1px solid rgba(255,255,255,.6)}
.news ul{list-style:none;position:absolute;left:18px;top:44px;font-size:11px;font-family:"Arimo",sans-serif}
.news li{margin-bottom:6px;letter-spacing:.3px}
.news li:nth-child(3){margin-left:-2px;margin-top:2px}
.news li:nth-child(2){margin-left:-1px}
.footer{position:absolute;left:329px;top:693px;width:622px;height:195px;background:var(--grey-dark);color:var(--white)}
.footer-col{position:absolute;list-style:none}
.footer-col h3{font-weight:700}
.about{left:32px;top:18px;font-size:11px;line-height:15px}
.about h3{font-size:13px;margin-bottom:14px}
.help{left:256px;top:20px;font-size:14px;line-height:17px}
.help h3{font-size:16px;margin-bottom:14px}
.talk{left:425px;top:18px;font-size:16px;line-height:19px}
.talk h3{font-size:17px;margin-bottom:14px}
</style>
</head>
<body>
<div class="page"></div>

<header class="header">
  <nav class="top-links">
    <a style="left:596px">Create Account</a>
    <a style="left:699px">Sign In</a>
    <a style="left:767px">Help</a>
  </nav>
</header>
<div class="brand"><span class="brand-mark"></span><span class="brand-name">Hardolen.to</span></div>
<div class="search">
  <div class="search-field">search for
    <svg width="16" height="16" viewBox="0 0 16 16"><circle cx="6.5" cy="6.5" r="4.5" fill="none" stroke="#555" stroke-width="1.6"/><line x1="10" y1="10" x2="14.5" y2="14.5" stroke="#555" stroke-width="2"/></svg>
  </div>
</div>

<section class="banner">
  <div class="banner-stage">
    <div class="mascot" role="img" aria-label="White line drawing of a smiling mascot giving a thumbs up"></div>
    <span class="circle" style="left:456px;top:0;width:114px;height:114px"></span>
    <span class="circle" style="left:541px;top:101px;width:80px;height:80px"></span>
    <span class="circle" style="left:384px;top:122px;width:104px;height:104px"></span>
    <span class="circle" style="left:543px;top:201px;width:48px;height:48px"></span>
    <div class="learn-more">Learn more
      <svg width="28" height="16" viewBox="0 0 28 16"><path d="M3 1l8 7-8 7M13 1l8 7-8 7" fill="none" stroke="#ddd" stroke-width="1.6"/></svg>
    </div>
  </div>
  <div class="banner-strip"></div>
  <div class="dots"><span></span><span></span><span></span><span class="active"></span><span></span></div>
  <svg class="next" width="34" height="18" viewBox="0 0 34 18"><path d="M2 1l8 8-8 8M12 1l8 8-8 8M22 1l8 8-8 8" fill="none" stroke="#ddd" stroke-width="1.4"/></svg>
  <div class="social"><span></span><span></span><span></span></div>
</section>

<main class="content">
  <h1>YOUR INFORMACTIO</h1>
  <p class="intro">(example line) Whether you want the simplest, most robust tools to turn your media social, or to find the right audience for your advertising message, SpreadWell puts sharing to work for you. Use the most innovative social media and sharing platform for the Web, SpreadWell. - See more at: http://spreadwell.net/#swhash.qk4RtLpz.dpuf</p>

  <section class="news news-orange">
    <h2>WHAT'S NEW</h2><hr>
    <ul><li>In Memoriam »</li><li>Weekly Top Shares, 5-31-2013 »</li><li>SpreadWell Takes Home Some Hard... »</li></ul>
  </section>
  <section class="news news-dark">
    <h2 style="top:2px">WHAT'S NEW</h2><hr style="top:28px">
    <ul style="top:40px"><li>In Memoriam »</li><li>Weekly Top Shares, 5-31-2013 »</li><li>SpreadWell Takes Home Some Hard... »</li></ul>
  </section>
</main>

<footer class="footer">
  <ul class="footer-col about">
    <h3>ABOUT US</h3>
    <li>Team</li><li>Careers</li><li>Contact Us</li><li>Privacy | Opt Out</li><li>Terms of Service</li><li>Publisher Terms of Service</li><li>Our Privacy Manifesto</li><li>Usage Guidelines</li><li>News</li>
  </ul>
  <ul class="footer-col help">
    <h3>HELP</h3>
    <li>Customization</li><li>Analytics</li><li>Integration</li><li>API</li><li>Sharing Services</li><li>System Status</li>
  </ul>
  <ul class="footer-col talk">
    <h3>TALK TO US</h3>
    <li>Blog</li><li>Forums</li><li>Feedback</li>
  </ul>
</footer>
</body>
</html>
```